Business Card Design

Need business card design for all carpentry & construction solutions. We would like to see designs that use black as a background with orange writing as it would stand out.

Business

KRV CONTRACTING
MARTIN COLBY
14 PELLINGTON ST
MARRELLA DOWNS
WA 6718
0498371265
krvcontracting@tramlex.com

```html
<!DOCTYPE html>
<html lang="en">
<head>
<meta charset="utf-8">
<title>KRV Contracting – Business Card</title>
<link rel="stylesheet" href="https://fonts.googleapis.com/css2?family=Lato:wght@400;700&display=swap">
<style>
  :root {
    --card-bg: #000000;
    --accent: #f5a02a;
  }
  html, body {
    margin: 0;
    padding: 0;
    width: 1200px;
    height: 742px;
    overflow: hidden;
    background: var(--card-bg);
  }
  .card {
    position: relative;
    width: 1200px;
    height: 742px;
    background: var(--card-bg);
    color: var(--accent);
    font-family: "Lato", sans-serif;
  }
  .brand-mark {
    position: absolute;
    left: 120px;
    top: 270px;
    width: 400px;
    height: 130px;
    display: flex;
    align-items: center;
    justify-content: center;
    gap: 22px;
  }
  .brand-mark__square {
    width: 34px;
    height: 34px;
    border: 6px solid var(--accent);
    box-sizing: border-box;
  }
  .brand-mark__name {
    font-weight: 700;
    font-size: 84px;
    letter-spacing: 4px;
    line-height: 1;
  }
  .company {
    position: absolute;
    left: 601px;
    top: 130px;
    margin: 0;
    font-weight: 400;
    font-size: 41px;
    line-height: 1;
    letter-spacing: 0.5px;
  }
  .person {
    position: absolute;
    left: 601px;
    top: 204px;
    margin: 0;
    font-weight: 700;
    font-size: 68px;
    line-height: 1;
    letter-spacing: 1px;
  }
  .divider {
    position: absolute;
    left: 601px;
    right: 0;
    top: 312px;
    height: 6px;
    background: var(--accent);
  }
  .contact {
    position: absolute;
    left: 601px;
    top: 383px;
    margin: 0;
    padding: 0;
    list-style: none;
    font-weight: 400;
    font-size: 33px;
  }
  .contact li {
    height: 51px;
    line-height: 40px;
  }
  .contact .contact__state {
    padding-left: 6px;
  }
</style>
</head>
<body>
  <div class="card">
    <div class="brand-mark">
      <span class="brand-mark__square"></span>
      <span class="brand-mark__name">KRV</span>
    </div>

    <p class="company">KRV CONTRACTING</p>
    <h1 class="person">MARTIN COLBY</h1>
    <div class="divider"></div>

    <ul class="contact">
      <li>14 PELLINGTON ST</li>
      <li>MARRELLA DOWNS</li>
      <li class="contact__state">WA 6718</li>
      <li>0498371265</li>
      <li>krvcontracting@tramlex.com</li>
    </ul>
  </div>
</body>
</html>
```